High End Skincare for Women Cosmetics Brand

We need a wordpress website that is also a mobile-friendly website for our cosmetics company. We have 3 core products and have 10 dropship products to add. I have attached the pdf with brand guide and vision for the website.

Our mission - At Nora Vale we believe all women have four distinct characteristics; beauty, originality, passion, and confidence. Our beauty products simply enhance those qualities. We will always provide the safest products to our consumers and continue to uplift women around the world.

About us - NORA VALE IS AN ORGANIC COSMETICS AND SKINCARE BRAND WITH VARIOUS PRODUCTS TO ENHANCE YOUR NATURAL BEAUTY. WE ARE COMMITTED TO PROVIDING TIMELESS PRODUCTS THAT WILL BRING OUT THAT SPECIAL CONFIDENCE YOU FEEL AND DESIRE FROM COSMETICS THAT WILL PERFECTLY MESH YOUR LIFESTYLE. When you choose Nora Vale organic cosmetics and skincare products, you are choosing a product whose ingredients work perfectly with the most complicated natural skin. We want you to celebrate that unique natural beauty with Nora Vale organic cosmetics and skincare products that will enhance your beauty. We use the best quality plant-based and laboratory-made ingredients to produce the best organic products that will enhance your beauty and boost your confidence.

XoXo Nora Vale - We understand that beauty is much more than an outward appearance. Our unique products bring you confidence, courage, and enrich your spirit. True beauty is deeper, and we at Nora Vale seek to inspire you to discover that deep sense of beauty you always craved.

Style - Luxury High End / Should look expensive and feminine with a modern touch.
The logo files are attached to this.

Colors should be bold and bright that looks like luxury and modern.

The products we sell are organic skincare and cosmetic products.

The design should not include any images or generic types of a font that can be found in Microsoft Word.

Premium font required.

Nora Vale is a leading organic cosmetics and skincare brand with products that enhance the natural beauty of the everyday woman. Luxury without the luxe price tag.

Target Market(s)

Target audience women age 18- 42 Gen Y / Millennials / Gen X

Industry/Entity Type

Beauty

Number of Pages Required

4 page

Font styles to use
Sans Serif

Colors

Designer to choose colors to be used in the design.

Requirements
Must have
• Must have images of women of diverse ethnicity at least 4 women
• Must have images of products -
• Must have an option to integrate dropship product links
• Must have contact us form
• Must have about us page
• Must have high-resolution images
• Must have a feature to check out on the website
• Must be mobile friendly
Nice to have
• Nice to have blog feature
• Nice to have a chat bot

```html
<!DOCTYPE html>
<html lang="en">
<head>
<meta charset="utf-8">
<title>Nora Vale — Organic Cosmetics &amp; Skincare</title>
<link rel="stylesheet" href="https://fonts.googleapis.com/css2?family=Montserrat:wght@400;500;600;700&family=Open+Sans:wght@400;600;700&display=swap">
<style>
:root{
  --ink:#0d0c17;
  --ink-soft:#1c1b27;
  --pink:#ea5169;
  --text:#1d1d24;
  --muted:#8a8a93;
  --strip:#f1f1f1;
  --white:#ffffff;
  --rose-card:#f2e4e6;
  --lilac-card:#e5e6f1;
  --mint-card:#e4f0ef;
  --line:#d8d8dc;
}
*{box-sizing:border-box;margin:0;padding:0}
html,body{width:1200px;height:3930px;overflow:hidden;background:var(--white)}
body{position:relative;font-family:"Open Sans",sans-serif;color:var(--text)}
.abs{position:absolute}

/* top bar */
.topbar{left:0;top:0;width:1200px;height:32px;background:var(--ink);color:var(--white);font:700 13px "Montserrat",sans-serif;letter-spacing:.3px;display:flex;align-items:center;justify-content:center}

/* hero */
.hero{left:0;top:32px;width:1200px;height:542px;background:var(--ink);overflow:hidden}
.hero-photo{position:absolute;left:560px;top:0;width:640px;height:542px;background:radial-gradient(ellipse at 55% 45%,#8a5a3e 0%,#4a2d20 35%,#171015 70%,var(--ink) 100%)}
.brand{font:400 26px "Montserrat",sans-serif;letter-spacing:6px;color:var(--white);white-space:nowrap}
.nav{position:absolute;top:30px;left:0;width:1200px;height:40px}
.nav .brand{position:absolute;left:100px;top:2px}
.menu{position:absolute;left:362px;top:10px;display:flex;gap:34px;font:500 15px "Montserrat",sans-serif;color:var(--white)}
.nav-tools{position:absolute;left:910px;top:8px;display:flex;gap:22px;align-items:center;color:var(--white);font:600 11px "Montserrat",sans-serif}
.hero-title{position:absolute;left:122px;top:150px;font:600 48px/1.15 "Montserrat",sans-serif;color:var(--white);letter-spacing:-.5px}
.mark{position:relative;display:inline-block}
.mark::after{content:"";position:absolute;left:0;right:0;bottom:2px;height:6px;background:var(--pink);border-radius:3px;z-index:-1}
.hero-title .mark::after{z-index:0;bottom:-4px;height:5px}
.btn-pink{background:var(--pink);color:var(--white);font:600 15px "Montserrat",sans-serif;display:flex;align-items:center;justify-content:center;letter-spacing:.5px}
.hero .btn-pink{position:absolute;left:122px;top:368px;width:244px;height:58px}

/* features */
.features{left:0;top:576px;width:1200px;height:84px;background:var(--strip)}
.feature{display:flex;align-items:center;gap:18px;position:absolute;top:18px}
.feature h4{font:500 16px "Open Sans",sans-serif;color:var(--text)}
.feature p{font:400 13px "Open Sans",sans-serif;color:var(--pink);margin-top:2px}

/* promos */
.promo{top:694px;width:482px;height:301px;overflow:hidden}
.promo .photo{position:absolute;left:0;top:0;width:250px;height:301px}
.promo .copy{position:absolute;left:315px;top:70px;color:var(--white)}
.promo small{font:600 10px "Montserrat",sans-serif;letter-spacing:1px;display:block;margin-bottom:8px}
.promo h3{font:500 24px/1.15 "Montserrat",sans-serif}
.btn-outline-light{margin-top:30px;width:96px;height:24px;border:1px solid var(--white);font:600 8px "Montserrat",sans-serif;display:flex;align-items:center;justify-content:center;letter-spacing:1px}

/* section headings */
.section-title{left:0;width:1200px;text-align:center;font:500 46px "Montserrat",sans-serif;color:var(--ink)}

/* products */
.product{top:1263px;width:314px}
.product .stage{position:absolute;left:0;width:314px}
.product .item{position:absolute;border-radius:6px}
.product .name{position:absolute;top:340px;left:6px;font:400 21px "Open Sans",sans-serif;color:var(--text);white-space:nowrap}
.product .price{position:absolute;top:376px;left:6px;font:700 21px "Open Sans",sans-serif;color:var(--ink)}
.product .stars{position:absolute;top:381px;right:14px}
.btn-outline{border:2px solid var(--ink);font:600 16px "Montserrat",sans-serif;color:var(--ink);display:flex;align-items:center;justify-content:center;letter-spacing:.5px}

/* welcome */
.welcome-photo{left:136px;top:1926px;width:577px;height:419px;background:linear-gradient(90deg,#f2efec 0%,#e7c9b5 25%,#a06c50 50%,#e4c2ae 75%,#f3efec 100%)}
.welcome-copy{left:833px;top:1990px;width:300px}
.welcome-copy h2{font:600 44px/1.1 "Montserrat",sans-serif;color:var(--ink);white-space:nowrap}
.welcome-copy p{margin-top:22px;width:260px;font:400 15px/1.6 "Open Sans",sans-serif;color:#55555e}
.welcome-copy .more{margin-top:14px;font:400 14px "Open Sans",sans-serif;color:var(--pink);display:flex;gap:10px;align-items:center}

/* newsletter */
.newsletter{left:0;top:2350px;width:1200px;height:205px;background:var(--ink);color:var(--white)}
.newsletter h3{position:absolute;left:116px;top:40px;font:500 32px "Montserrat",sans-serif}
.newsletter h3 .mark::after{bottom:-4px;height:4px;z-index:0}
.newsletter .lead{position:absolute;left:116px;top:95px;font:400 19px "Open Sans",sans-serif}
.newsletter .note{position:absolute;left:116px;top:140px;font:400 11px "Open Sans",sans-serif;color:#b8b8c0}
.newsletter label{position:absolute;left:776px;top:36px;font:600 10px "Montserrat",sans-serif;letter-spacing:.5px}
.newsletter .field{position:absolute;left:776px;top:56px;width:308px;height:40px;border:1px solid #3b3a47;background:var(--ink-soft);font:400 14px "Open Sans",sans-serif;padding:9px 14px}
.newsletter .btn-pink{position:absolute;left:776px;top:112px;width:308px;height:44px;font-size:13px}

/* blog */
.post{top:2733px;width:283px}
.post .photo{width:283px;height:209px}
.post .date{margin-top:22px;font:400 15px "Open Sans",sans-serif;color:var(--muted)}
.post h4{margin-top:6px;font:600 24px/1.2 "Open Sans",sans-serif;color:var(--ink)}
.post p{margin-top:12px;font:400 15px/1.5 "Open Sans",sans-serif;color:#55555e}

/* contact */
.contact-title{left:200px;top:3332px;font:600 48px/1.1 "Montserrat",sans-serif;color:var(--ink)}
.contact-title .mark::after{bottom:2px;height:5px;z-index:-1}
.contact-info{left:200px;top:3520px;font:400 13px "Open Sans",sans-serif;color:var(--muted)}
.contact-info div{display:flex;gap:14px;align-items:center;margin-bottom:16px}
.input{border:1px solid var(--line);background:#f4f4f5;font:400 12px "Open Sans",sans-serif;color:var(--muted);display:flex;align-items:center;gap:10px;padding:0 14px}
.textarea{align-items:flex-start;padding-top:12px}

/* footer */
.footer-brand{left:0;width:1200px;top:3714px;text-align:center;font:400 30px "Montserrat",sans-serif;letter-spacing:10px;color:var(--ink)}
.follow{left:460px;top:3788px;display:flex;align-items:center;gap:22px;font:600 12px "Montserrat",sans-serif;letter-spacing:.5px;color:var(--ink)}
.social{width:16px;height:16px;border-radius:50%;background:var(--ink)}
.bottombar{left:0;top:3857px;width:1200px;height:73px;background:var(--strip);font:400 12px "Open Sans",sans-serif;color:#55555e}
.bottombar span{position:absolute;top:28px}
.card{width:38px;height:20px;border-radius:3px;background:#9a9aa3;display:inline-block}
</style>
</head>
<body>

<div class="abs topbar">FREE &amp; FAST SHIPPING FOR ALL ORDERS OVER $50</div>

<header class="abs hero">
  <div class="hero-photo" role="img" aria-label="Portrait of a woman with long wavy hair against a dark backdrop"></div>
  <nav class="nav">
    <div class="brand">NORA VALE</div>
    <div class="menu"><span>HOME</span><span>PRODUCTS</span><span>TUTORIALS</span><span>BLOG</span><span>CONTACT</span></div>
    <div class="nav-tools">
      <svg width="16" height="16" viewBox="0 0 16 16" fill="none" stroke="#fff" stroke-width="1.6"><circle cx="7" cy="7" r="5"/><path d="M11 11l4 4"/></svg>
      <span>ENG ▾</span><span>USD ▾</span>
      <svg width="20" height="20" viewBox="0 0 20 20" fill="none" stroke="#fff" stroke-width="1.5"><path d="M4 6h12l-1 11H5z"/><path d="M7 6a3 3 0 0 1 6 0"/><circle cx="16" cy="15" r="3.5" fill="#ea5169" stroke="none"/></svg>
    </div>
  </nav>
  <h1 class="hero-title"><span class="mark">enhance</span><br>the beauty<br>within</h1>
  <div class="btn-pink">SHOP NOW</div>
</header>

<section class="abs features">
  <div class="feature" style="left:108px">
    <svg width="34" height="28" viewBox="0 0 34 28" fill="none" stroke="#ea5169" stroke-width="1.8"><path d="M2 5h19v14H2zM21 10h6l5 5v4h-11"/><circle cx="8" cy="21" r="3" fill="#fff"/><circle cx="26" cy="21" r="3" fill="#fff"/></svg>
    <div><h4>Free Shipping And Return</h4><p>All order over $50</p></div>
  </div>
  <div class="feature" style="left:476px">
    <svg width="32" height="32" viewBox="0 0 32 32" fill="none" stroke="#ea5169" stroke-width="1.8"><path d="M26 12A11 11 0 0 0 6 10M6 20a11 11 0 0 0 20 2"/><path d="M6 4v6h6M26 28v-6h-6"/></svg>
    <div><h4>100% Money Guarantee</h4><p>Secure payment</p></div>
  </div>
  <div class="feature" style="left:830px">
    <svg width="32" height="32" viewBox="0 0 32 32" fill="none" stroke="#ea5169" stroke-width="1.8"><circle cx="16" cy="18" r="11"/><path d="M16 11v7l5 3M4 7l5-4M28 7l-5-4"/></svg>
    <div><h4>Fast And Reliable Support</h4><p>Support 24/7</p></div>
  </div>
</section>

<section>
  <div class="abs promo" style="left:100px;background:#a9dcdf">
    <div class="photo" role="img" aria-label="Woman with long dark hair in a floral top on a light teal background" style="background:linear-gradient(90deg,#a9dcdf 0%,#c58f6c 45%,#a9dcdf 100%)"></div>
    <div class="copy"><small>TUTORIAL VIDEOS</small><h3>learn from<br>our<br>experts</h3><div class="btn-outline-light">LEARN MORE</div></div>
  </div>
  <div class="abs promo" style="left:618px;background:#e8e6d2">
    <div class="photo" role="img" aria-label="Surprised woman with curly blonde hair on a soft cream background" style="left:232px;background:linear-gradient(90deg,#e8e6d2 0%,#d9b27a 45%,#e9c2a8 75%,#e8e6d2 100%)"></div>
    <div class="copy" style="left:50px"><small>NEW ARRIVALS</small><h3>don't miss<br>our latest<br>products</h3><div class="btn-outline-light">SHOP NOW</div></div>
  </div>
</section>

<h2 class="abs section-title" style="top:1100px">Our Products</h2>

<section>
  <div class="abs product" style="left:100px">
    <div class="stage" style="top:0;height:325px;background:var(--rose-card)"></div>
    <div class="item" role="img" aria-label="Black pump bottle of Nora Vale Oil Cleanser" style="left:106px;top:-55px;width:104px;height:330px;background:linear-gradient(90deg,#1a1a1f,#3b3b42 50%,#1a1a1f)"></div>
    <div class="name">NORA VALE Oil Cleanser</div><div class="price">$19.99</div>
    <svg class="stars" width="70" height="12" viewBox="0 0 70 12"><g fill="#ea5169"><circle cx="6" cy="6" r="5"/><circle cx="20" cy="6" r="5"/><circle cx="34" cy="6" r="5"/><circle cx="48" cy="6" r="5"/></g><circle cx="62" cy="6" r="5" fill="#ccc"/></svg>
  </div>
  <div class="abs product" style="left:464px">
    <div class="stage" style="top:131px;height:194px;background:var(--lilac-card)"></div>
    <div class="item" role="img" aria-label="Black jar of Nora Vale Face Moisturizer" style="left:82px;top:104px;width:150px;height:120px;background:linear-gradient(90deg,#18181d,#3a3a42 50%,#18181d)"></div>
    <div class="name">NORA VALE Face Moisturizer</div><div class="price">$15.99</div>
    <svg class="stars" width="70" height="12" viewBox="0 0 70 12"><g fill="#ea5169"><circle cx="6" cy="6" r="5"/><circle cx="20" cy="6" r="5"/><circle cx="34" cy="6" r="5"/><circle cx="48" cy="6" r="5"/></g><circle cx="62" cy="6" r="5" fill="#ccc"/></svg>
  </div>
  <div class="abs product" style="left:807px">
    <div class="stage" style="top:131px;height:194px;background:var(--mint-card)"></div>
    <div class="item" role="img" aria-label="Black jar of Nora Vale Charcoal Mask" style="left:82px;top:104px;width:150px;height:120px;background:linear-gradient(90deg,#18181d,#3a3a42 50%,#18181d)"></div>
    <div class="name">NORA VALE Charcoal Mask</div><div class="price">$19.99</div>
    <svg class="stars" width="70" height="12" viewBox="0 0 70 12"><g fill="#ea5169"><circle cx="6" cy="6" r="5"/><circle cx="20" cy="6" r="5"/><circle cx="34" cy="6" r="5"/><circle cx="48" cy="6" r="5"/></g><circle cx="62" cy="6" r="5" fill="#ccc"/></svg>
  </div>
</section>

<div class="abs btn-outline" style="left:477px;top:1750px;width:246px;height:58px">SHOP NOW</div>

<section>
  <div class="abs welcome-photo" role="img" aria-label="Three smiling women of diverse ethnicity in nude-toned tops"></div>
  <div class="abs welcome-copy">
    <h2><span class="mark">welcome</span><br>NORA VALE</h2>
    <p>We are your leading organic cosmetics and skincare brand that offer products that enhance and nourish your skin.</p>
    <div class="more">Learn more <svg width="12" height="12" viewBox="0 0 12 12"><circle cx="6" cy="6" r="5.5" fill="#ea5169"/><path d="M5 3.5L7.5 6 5 8.5" stroke="#fff" stroke-width="1.3" fill="none"/></svg></div>
  </div>
</section>

<section class="abs newsletter">
  <h3><span class="mark">Subscribe</span> to our newsletter</h3>
  <div class="lead">And get great discouts offers!</div>
  <div class="note">* You need to confirm the action to the email address</div>
  <label>YOUR E-MAIL</label>
  <div class="field">mara.lin|</div>
  <div class="btn-pink">SUBSCRIBE</div>
</section>

<h2 class="abs section-title" style="top:2618px">Blog &amp; News</h2>

<section>
  <article class="abs post" style="left:120px">
    <div class="photo" role="img" aria-label="Woman with curly hair on a pink background" style="background:linear-gradient(135deg,#f3b9c6,#8d4a35 55%,#f0c1cc)"></div>
    <div class="date">Mars 02, 2019</div><h4>Lorem Ipsum</h4>
    <p>Suspendisse nunc odio, varius et consectetur et, dignissim a dui. In luctus risus orci.</p>
  </article>
  <article class="abs post" style="left:464px">
    <div class="photo" role="img" aria-label="Blonde woman with soft curls on a grey background" style="background:linear-gradient(135deg,#9c9c9f,#e1c9a2 50%,#bdbcbd)"></div>
    <div class="date">Mars 01, 2019</div><h4>Donec Lobortis</h4>
    <p>Fusce eget enim at purus sagittis finibus ac ut nisl.</p>
  </article>
  <article class="abs post" style="left:796px">
    <div class="photo" role="img" aria-label="Woman with pink hair and pink manicure" style="background:linear-gradient(135deg,#e7a3ad,#f0d2c6 50%,#ededf0)"></div>
    <div class="date">Mars 02, 2019</div><h4>Ut Pellentesque Dui Vel Leo Facilisis</h4>
    <p>Praesent scelerisque libero urna...</p>
  </article>
</section>

<div class="abs btn-outline" style="left:477px;top:3147px;width:246px;height:58px">VIEW ALL</div>

<section>
  <h2 class="abs contact-title"><span class="mark">get in</span><br>touch<br>with us</h2>
  <div class="abs contact-info">
    <div><svg width="12" height="12" viewBox="0 0 12 12"><path d="M2 1h3l1 3-2 1a7 7 0 0 0 3 3l1-2 3 1v3a1 1 0 0 1-1 1A10 10 0 0 1 1 2a1 1 0 0 1 1-1z" fill="#ea5169"/></svg>+1 555-014-2290</div>
    <div><svg width="12" height="10" viewBox="0 0 12 10"><rect width="12" height="10" rx="1" fill="#ea5169"/><path d="M1 1l5 4 5-4" stroke="#fff" fill="none"/></svg>info@noravale.com</div>
  </div>
  <div class="abs input" style="left:582px;top:3343px;width:204px;height:40px"><svg width="11" height="12" viewBox="0 0 11 12" fill="#9a9aa3"><circle cx="5.5" cy="3" r="3"/><path d="M0 12a5.5 5 0 0 1 11 0z"/></svg>Name</div>
  <div class="abs input" style="left:797px;top:3343px;width:204px;height:40px"><svg width="12" height="10" viewBox="0 0 12 10"><rect width="12" height="10" rx="1" fill="#9a9aa3"/><path d="M1 1l5 4 5-4" stroke="#f4f4f5" fill="none"/></svg>E-mail</div>
  <div class="abs input textarea" style="left:582px;top:3396px;width:419px;height:157px">Your Message</div>
  <div class="abs btn-pink" style="left:582px;top:3569px;width:140px;height:42px;font-size:12px">SEND</div>
</section>

<footer>
  <div class="abs footer-brand">NORA VALE</div>
  <div class="abs follow">FOLLOW <span class="social"></span><span class="social"></span><span class="social"></span><span class="social"></span><span class="social"></span></div>
  <div class="abs bottombar">
    <span style="left:98px">© 2019 NORA VALE. All rights reserved.</span>
    <span style="left:458px;top:24px;display:flex;gap:12px;align-items:center">Payment Options: <i class="card"></i><i class="card"></i><i class="card"></i><i class="card"></i></span>
    <span style="left:922px">Terms of Use</span>
    <span style="left:1022px">Privacy Policy</span>
  </div>
</footer>

</body>
</html>
```